Business Card 85x40mm - Freelance audio mixing / live event operator

I am a freelance audio operator working in live events. Mostly corporate events mixing sound for a range of entertainment, awards nights and functions. I need a new card to give to perspective clients.

The final design will convey bold professionalism with a general dark vibe. Looking for dark-ish background with some smatterings of colour added.

I have attatched my old BC for an idea of what I have liked in the past. Id like a more modern updated design (that circular design on the back is not my logo it is just a picture I found that resembled sound} . For an added element possibly a mixture of some playful colours in a way that resembles an audio wave form or sound.

I have attached a photo called "audio software" with some colourful squiggly lines; maybe incorporate elements of that into into design
Updates

Added extra $ to project Damn Pixel hives fees are unreasonable

Target Market(s)

Mostly corporate clients

Industry/Entity Type

Events

Contact Information for Business Card

Corwin Pellath
Sound | FOH | Monitors | Systems | Corporate

Digital Audio Mixing Specialist, Live Event Technical Professional,

corwinpellath@mailvexo.net, +61 402 918 357

Colors
ec1f27
ffc214
9bcb3c
6b449b

Requirements
Must have
• Dark theme
• 85x40mm dimensions
Nice to have
• some sort of imagery or design to reflect audio/sound

```html
<!DOCTYPE html>
<html lang="en">
<head>
<meta charset="utf-8">
<title>Corwin Pellath – Business Card</title>
<link rel="stylesheet" href="https://fonts.googleapis.com/css2?family=Open+Sans:wght@400&family=Orbitron:wght@500&display=swap">
<style>
  :root {
    --canvas: #ffffff;
    --frame: #c9c9c9;
    --card-dark: #000000;
    --red: #ec1f27;
    --yellow: #ffc214;
    --green: #9bcb3c;
    --purple: #6b449b;
    --white: #ffffff;
    --ink: #1a1a1a;
  }
  * { margin: 0; padding: 0; box-sizing: border-box; }
  html, body { width: 1200px; height: 1200px; overflow: hidden; }
  body {
    position: relative;
    background: var(--canvas);
    border: 1px solid var(--frame);
    font-family: "Open Sans", Arial, sans-serif;
  }
  .card {
    position: absolute;
    left: 99px;
    width: 1002px;
    height: 471px;
    overflow: hidden;
    background: var(--card-dark);
  }
  .card--front { top: 79px; }
  .card--back { top: 650px; }

  .waveform-art { position: absolute; inset: 0; }
  .card--front .waveform-art {
    background:
      radial-gradient(ellipse 40% 50% at 15% 30%, rgba(236,31,39,.75), transparent 70%),
      radial-gradient(ellipse 35% 45% at 45% 25%, rgba(255,194,20,.7), transparent 70%),
      radial-gradient(ellipse 35% 45% at 70% 40%, rgba(230,230,220,.45), transparent 70%),
      radial-gradient(ellipse 35% 40% at 65% 85%, rgba(155,203,60,.65), transparent 70%),
      radial-gradient(ellipse 30% 40% at 92% 80%, rgba(107,68,155,.75), transparent 70%),
      radial-gradient(ellipse 30% 40% at 15% 85%, rgba(200,200,200,.4), transparent 70%),
      var(--card-dark);
  }
  .card--back .waveform-art {
    background:
      radial-gradient(ellipse 18% 22% at 8% 78%, rgba(236,31,39,.8), transparent 70%),
      radial-gradient(ellipse 18% 25% at 32% 68%, rgba(245,130,32,.7), transparent 70%),
      radial-gradient(ellipse 16% 25% at 45% 58%, rgba(255,194,20,.7), transparent 70%),
      radial-gradient(ellipse 16% 28% at 60% 45%, rgba(155,203,60,.6), transparent 70%),
      radial-gradient(ellipse 16% 25% at 78% 25%, rgba(200,200,200,.35), transparent 70%),
      radial-gradient(ellipse 16% 22% at 95% 12%, rgba(107,68,155,.6), transparent 70%),
      var(--card-dark);
  }

  .tagline {
    position: absolute;
    left: 91px;
    top: 214px;
    height: 42px;
    padding: 0 10px;
    background: var(--white);
    color: var(--ink);
    font-size: 26px;
    line-height: 42px;
    white-space: nowrap;
  }
  .divider { color: var(--red); padding: 0 10px; }

  .name {
    position: absolute;
    left: 38px;
    top: 42px;
    color: var(--red);
    font-family: "Orbitron", "Arial Black", sans-serif;
    font-weight: 500;
    font-size: 30px;
    letter-spacing: 6px;
    text-transform: uppercase;
    white-space: nowrap;
  }
  .services {
    position: absolute;
    left: 38px;
    top: 88px;
    color: var(--white);
    font-size: 26px;
    white-space: nowrap;
  }
  .services .divider { padding: 0 6px; }

  .contact {
    position: absolute;
    right: 42px;
    top: 376px;
    list-style: none;
    color: var(--white);
    font-size: 26px;
    line-height: 35px;
    text-align: right;
  }
  .contact li { display: flex; align-items: center; justify-content: flex-end; gap: 8px; }
  .contact svg { width: 26px; height: 26px; }
</style>
</head>
<body>
  <section class="card card--front">
    <div class="waveform-art" role="img" aria-label="Glowing colourful audio waveform lines in red, yellow, white, green and purple on black"></div>
    <p class="tagline">Digital Audio Mixing Specialist<span class="divider">|</span>Live Event Technical Professional</p>
  </section>

  <section class="card card--back">
    <div class="waveform-art" role="img" aria-label="Diagonal band of glowing audio waveform lines fading from red through yellow and green to purple"></div>
    <h1 class="name">Corwin Pellath</h1>
    <p class="services">Sound<span class="divider">|</span>FOH<span class="divider">|</span>Monitors<span class="divider">|</span>Systems<span class="divider">|</span>Corporate</p>
    <ul class="contact">
      <li>+61 402 918 357
        <svg viewBox="0 0 26 26" aria-hidden="true"><circle cx="13" cy="13" r="11.5" fill="#111" stroke="#bbb" stroke-width="1.5"/><rect x="9.5" y="6" width="7" height="14" rx="1.5" fill="var(--red)"/><rect x="10.8" y="8" width="4.4" height="8.5" fill="#111"/></svg>
      </li>
      <li>corwinpellath@mailvexo.net
        <svg viewBox="0 0 26 26" aria-hidden="true"><circle cx="13" cy="13" r="11.5" fill="#111" stroke="#bbb" stroke-width="1.5"/><rect x="6.5" y="8.5" width="13" height="9" fill="var(--red)"/><path d="M6.5 8.5 L13 14 L19.5 8.5" fill="none" stroke="#fff" stroke-width="1.2"/></svg>
      </li>
    </ul>
  </section>
</body>
</html>
```